brolvin business card design so that it looks better

need a new business card designed. use our website, brolvix.example for example. I attached an example of a previous card we had and liked. this is for law enforcement and we have attached a previous business card as an example. This site forces me to select color and font, ignore those as I picked stuff just to get this completed.

Target Market(s)

law enforcement, local government

Contact Information for Business Card

see the attached example and our website

Font styles to use
Serif

```html
<!DOCTYPE html>
<html lang="en">
<head>
<meta charset="utf-8">
<title>Brolvin Business Card</title>
<link rel="stylesheet" href="https://fonts.googleapis.com/css2?family=Montserrat:wght@700;800&family=Roboto:wght@300;400;500&display=swap">
<style>
  :root {
    --backdrop: #232323;
    --card: #0f2230;
    --card-edge: #0b1a25;
    --map-glow: #3f8fd0;
    --map-deep: #123a56;
    --text-light: #ffffff;
    --text-soft: #e4ecf2;
    --accent-blue: #2f7fcf;
  }
  * { margin: 0; padding: 0; box-sizing: border-box; }
  html, body {
    width: 1200px; height: 1200px; overflow: hidden;
    background: var(--backdrop);
  }
  .canvas {
    position: relative; width: 1200px; height: 1200px;
    background: radial-gradient(circle at 50% 40%, #2b2b2b, var(--backdrop) 70%);
  }
  .card {
    position: absolute; left: 150px; width: 900px; height: 514px;
    border-radius: 28px;
    background: linear-gradient(160deg, #13293a, var(--card) 55%, var(--card-edge));
    box-shadow: 0 18px 40px rgba(0,0,0,.55);
    overflow: hidden;
  }
  .card--front { top: 66px; }
  .card--back { top: 620px; }

  .map-area {
    position: absolute; left: 130px; top: 40px; width: 690px; height: 420px;
    border-radius: 45% 40% 35% 30% / 40% 35% 55% 45%;
    background: radial-gradient(ellipse at 55% 70%, rgba(90,180,240,.75), var(--map-glow) 25%, var(--map-deep) 65%, rgba(18,58,86,0) 90%);
    opacity: .85;
  }
  .front-content {
    position: absolute; inset: 0;
    display: flex; flex-direction: column; align-items: center; justify-content: center;
    text-align: center; color: var(--text-light);
    padding-top: 10px;
  }
  .front-brand {
    font-family: "Roboto", sans-serif; font-weight: 300;
    font-size: 64px; letter-spacing: 10px; line-height: 1;
    margin-bottom: 8px;
  }
  .front-headline {
    font-family: "Montserrat", sans-serif; font-weight: 800;
    font-size: 52px; line-height: 1.02; letter-spacing: 1px;
  }
  .front-tagline {
    font-family: "Montserrat", sans-serif; font-weight: 700;
    font-size: 17px; margin-top: 10px; letter-spacing: .3px;
  }

  .contact {
    position: absolute; left: 96px; top: 110px;
    font-family: "Roboto", sans-serif; color: var(--text-light);
  }
  .contact__name { font-size: 30px; font-weight: 400; }
  .contact__role { font-size: 21px; font-weight: 400; color: var(--accent-blue); margin-top: 2px; }
  .contact__address { font-size: 21px; line-height: 1.3; margin-top: 20px; color: var(--text-soft); }
  .contact__list { list-style: none; margin-top: 18px; }
  .contact__item {
    display: flex; align-items: center; gap: 14px;
    font-size: 22px; line-height: 1.35; color: var(--text-soft);
  }
  .contact__icon { width: 20px; height: 20px; flex: none; }

  .back-brand {
    position: absolute; right: 90px; top: 290px;
    font-family: "Roboto", sans-serif; font-weight: 300;
    font-size: 70px; letter-spacing: 12px; color: var(--text-light);
  }
</style>
</head>
<body>
<main class="canvas">
  <section class="card card--front">
    <div class="map-area" role="img" aria-label="Glowing network map of the United States with connected points"></div>
    <div class="front-content">
      <div class="front-brand">BROLVIN</div>
      <h1 class="front-headline">LAW ENFORCEMENT<br>INNOVATION</h1>
      <p class="front-tagline">Automating Processes and Connecting Jurisdictions</p>
    </div>
  </section>

  <section class="card card--back">
    <div class="contact">
      <p class="contact__name">Marcus Delane</p>
      <p class="contact__role">CEO/Founder</p>
      <p class="contact__address">1420 Larkspur Avenue<br>Fairview, TX 75069</p>
      <ul class="contact__list">
        <li class="contact__item">
          <svg class="contact__icon" viewBox="0 0 24 24" aria-hidden="true"><path fill="#2f7fcf" d="M6.6 10.8a15.1 15.1 0 0 0 6.6 6.6l2.2-2.2c.3-.3.7-.4 1-.2 1.1.4 2.3.6 3.6.6.6 0 1 .4 1 1V20c0 .6-.4 1-1 1A17 17 0 0 1 3 4c0-.6.4-1 1-1h3.5c.6 0 1 .4 1 1 0 1.3.2 2.5.6 3.6.1.3 0 .7-.2 1z"/></svg>
          800.555.0142
        </li>
        <li class="contact__item">
          <svg class="contact__icon" viewBox="0 0 24 24" aria-hidden="true"><rect x="2" y="5" width="20" height="14" rx="1.5" fill="#2f7fcf"/><path d="M3 6l9 7 9-7" fill="none" stroke="#0f2230" stroke-width="1.6"/></svg>
          info@brolvix.example
        </li>
        <li class="contact__item">
          <svg class="contact__icon" viewBox="0 0 24 24" aria-hidden="true"><g fill="none" stroke="#2f7fcf" stroke-width="1.6"><circle cx="12" cy="12" r="9.5"/><ellipse cx="12" cy="12" rx="4.2" ry="9.5"/><path d="M2.5 12h19M4 7h16M4 17h16"/></g></svg>
          brolvix.example
        </li>
      </ul>
    </div>
    <div class="back-brand">BROLVIN</div>
  </section>
</main>
</body>
</html>
```